Web Design Project and logo

We need a new web design and logo for www.kq7ventra.com

It is a mobile app development company. Site needs to look very cool/trendy as does the new logo.

Looking for the design (uncoded) and the logo file that my developers can then use to build out the site.

An example of a nice competitor site is www.plumwirestudio.com

We want something that looks fresh, clean and hip.

Also development of business cards.

Target Market(s)

Small to mid sized companies

Industry/Entity Type

Business

Requirements
Must have
• Ability to request a quote
Should look very trendy like www.plumwirestudio.com as an example of a competitor site

```html
<!DOCTYPE html>
<html lang="en">
<head>
<meta charset="utf-8">
<title>KQ7 Ventra – Mobile App Development</title>
<link href="https://fonts.googleapis.com/css2?family=Open+Sans:wght@300;400;600;700&display=swap" rel="stylesheet">
<style>
:root{
  --stage-light:#8c8886;
  --stage-dark:#646160;
  --accent:#f04b33;
  --ink:#3b3b3b;
  --muted:#8a8a8a;
  --pale:#f3f3f3;
  --pale-2:#ececec;
  --white:#ffffff;
  --night:#0d0d0f;
  --icon:#5a6470;
}
*{box-sizing:border-box;margin:0;padding:0}
html,body{width:1200px;height:1000px;overflow:hidden}
body{
  font-family:"Open Sans",Arial,sans-serif;
  background:radial-gradient(ellipse at 50% 45%,var(--stage-light) 0%,var(--stage-dark) 80%);
  position:relative;color:var(--ink);
}
.page{position:absolute;left:386px;top:10px;width:427px;height:974px;background:var(--white);overflow:hidden;box-shadow:0 0 18px rgba(0,0,0,.25)}
.abs{position:absolute}

/* nav */
.topbar{left:0;top:0;width:427px;height:24px;background:var(--white);font-size:5px;color:var(--muted)}
.brand{left:10px;top:3px;display:flex;align-items:center;gap:3px}
.brand-mark{width:9px;height:9px;background:var(--accent)}
.brand-name{font-weight:700;font-size:9px;color:var(--accent);letter-spacing:.2px}
.nav{left:84px;top:8px;display:flex;gap:10px}
.nav .active{color:var(--ink)}
.call{left:255px;top:8px}
.lang{left:326px;top:8px}
.quote-btn{left:371px;top:5px;width:44px;height:13px;border:1px solid #c9c9c9;border-radius:2px;background:linear-gradient(#f7f7f7,#dcdcdc);text-align:center;line-height:11px;color:#777}

/* hero */
.hero{left:0;top:24px;width:427px;height:247px;
  background:
   linear-gradient(90deg,rgba(120,60,45,.35) 0%,rgba(13,13,15,0) 45%,rgba(150,50,30,.35) 100%),
   linear-gradient(180deg,#141214 0%,var(--night) 60%,#1c2a48 100%)}
.hero-title{left:0;top:73px;width:427px;text-align:center;color:var(--white);font-weight:300;font-size:18px;letter-spacing:.3px}
.hero-sub{left:75px;top:95px;width:276px;height:11px;background:rgba(0,0,0,.8);color:#ddd;font-size:4.6px;text-align:center;line-height:11px}
.btn{top:118px;width:66px;height:19px;background:var(--accent);color:var(--white);font-size:5px;font-weight:600;text-align:center;line-height:19px}
.features{left:4px;top:206px;width:419px;height:36px;display:flex;gap:10px}
.feature{flex:1;background:rgba(0,0,0,.6);display:flex;gap:6px;padding:6px 5px;color:var(--white)}
.feature svg{flex:none}
.feature h4{font-size:4.6px;font-weight:600}
.feature p{font-size:3.8px;line-height:5px;color:#ccc;margin-top:1px}

/* intro */
.intro{left:0;top:271px;width:427px;height:44px;background:var(--pale);text-align:center}
.intro h2{font-weight:400;font-size:9px;margin-top:11px;color:var(--ink)}
.intro h2 span{display:block;color:var(--accent);font-size:8px;font-weight:600;line-height:9px}

/* services */
.services{left:0;top:315px;width:427px;height:123px;background:var(--pale);display:flex}
.service{width:85.4px;border-left:1px solid #e2e2e2;text-align:center;padding:23px 5px 0;position:relative}
.service h3{font-size:5px;font-weight:400;color:var(--muted);margin-top:10px;height:16px;line-height:6px}
.service p{font-size:4.3px;line-height:6px;text-align:left;color:var(--muted);margin-top:3px}
.service a{position:absolute;left:5px;bottom:12px;font-size:4.2px;color:var(--muted);font-style:italic}
.service.current{background:var(--accent);border:none}
.service.current h3,.service.current p,.service.current a{color:var(--white)}
.service.current::before{content:"";position:absolute;top:0;left:37px;border:6px solid transparent;border-top-color:var(--pale)}

/* about */
.about{left:0;top:438px;width:427px;height:142px;background:var(--white)}
.col-title{font-size:8px;font-weight:400;color:var(--ink)}
.col-text{font-size:4.4px;line-height:6px;color:var(--muted);margin-top:4px}
.more{font-size:4.4px;color:var(--muted);margin-top:8px}
.about-text{left:12px;top:32px;width:134px}
.video{left:157px;top:33px;width:128px;height:71px;background:linear-gradient(110deg,#23252b 0%,#2f3a4c 35%,#1f6fb3 70%,#48a8e0 100%)}
.play{left:50px;top:20px}
.testimonials{left:309px;top:32px;width:108px}
.avatars{display:flex;gap:8px;margin-top:5px}
.avatar{width:27px;height:29px;background:#b5b5b5}
.avatar.on{background:var(--accent)}

/* facts */
.facts-head{left:0;top:580px;width:427px;height:44px;background:var(--pale);text-align:center}
.facts-head h2{font-weight:400;font-size:8.5px;margin-top:11px}
.facts-head h2 span{display:block;color:var(--accent);font-size:7.5px;line-height:9px}
.facts{left:0;top:624px;width:427px;height:196px;background:var(--pale-2)}
.phone{left:44px;top:6px;width:91px;height:180px;border-radius:14px;background:linear-gradient(160deg,#2b2b2b,#0e0e0e 60%,#3a3a3a)}
.phone-screen{left:7px;top:25px;width:77px;height:126px;background:linear-gradient(#47a35e 0%,#3d6f93 45%,#d7d7d7 72%,#cfcfcf 100%)}
.laptop{left:269px;top:29px;width:158px;height:144px;background:linear-gradient(#1b1d20 0%,#1b1d20 88%,#c7c7c7 90%,#9d9d9d 100%)}
.laptop-screen{left:10px;top:9px;width:148px;height:116px;background:linear-gradient(135deg,#23282b,#2a3a2a 55%,#1d2123)}
.stats{left:150px;top:12px;width:130px;text-align:center;color:var(--ink)}
.stat b{display:block;font-size:9px;font-weight:700;line-height:9px}
.stat span{display:block;font-size:8.5px;font-weight:400;line-height:9px}
.op{font-size:14px;color:#bdbdbd;font-weight:300;line-height:32px}
.stat.red b{color:var(--accent)}

/* partners */
.partners{left:0;top:820px;width:427px;height:54px;background:var(--white);display:flex;align-items:center;justify-content:center;gap:14px}
.chev{color:#999;font-size:9px}
.badge{width:44px;height:12px;background:#c8c8c8;border-radius:2px}

/* footer */
.footer{left:0;top:874px;width:427px;height:83px;background:var(--pale)}
.f-title{font-size:4.6px;color:var(--muted);font-weight:600}
.f-text{font-size:4.4px;line-height:6px;color:var(--muted)}
.f-brand{left:12px;top:17px;width:110px}
.f-menu{left:139px;top:15px}
.f-menu ul{list-style:none;margin-top:8px}
.f-menu li{font-size:4.4px;color:var(--muted);line-height:8px}
.f-menu li.active{color:var(--ink)}
.f-contact{left:210px;top:15px;width:105px}
.f-row{display:flex;gap:6px;margin-top:6px}
.f-follow{left:319px;top:15px;width:100px}
.socials{display:flex;gap:5px;margin-top:9px}
.socials i{width:5px;height:5px;background:#9aa3ad;border-radius:1px}
.newsletter{margin-top:6px;width:95px;height:12px;background:var(--white);border:1px solid #ddd;font-size:4.2px;color:#999;line-height:10px;padding-left:3px;position:relative}
.newsletter::after{content:"";position:absolute;right:4px;top:3px;width:5px;height:4px;background:#999}
.copyright{left:0;top:957px;width:427px;height:17px;background:#000;color:#ddd;font-size:4.2px;text-align:center;line-height:17px}
</style>
</head>
<body>
<div class="page">

  <header class="topbar abs">
    <div class="brand abs"><span class="brand-mark"></span><span class="brand-name">KQ7</span></div>
    <nav class="nav abs"><span class="active">HOME</span><span>OUR SERVICES</span><span>LATEST NEWS</span><span>CONTACT</span></nav>
    <div class="call abs">CALL US ON: +00 000 0000</div>
    <div class="lang abs">ENGLISH ▾</div>
    <div class="quote-btn abs">I NEED APP NOW</div>
  </header>

  <section class="hero abs" role="img" aria-label="Photo of a fingertip touching a glowing touch screen">
    <h1 class="hero-title abs">THE NO1 APPS</h1>
    <p class="hero-sub abs">KQ7 Ventra helps you is a specialty mobile solutions provider with expertise across all the major mobile platforms.</p>
    <div class="btn abs" style="left:137px">SEE THE DETAILS NOW</div>
    <div class="btn abs" style="left:223px">I NEED APP NOW</div>
    <div class="features abs">
      <div class="feature">
        <svg width="16" height="16" viewBox="0 0 16 16" fill="none" stroke="#fff" stroke-width="1.2"><rect x="1" y="2" width="9" height="12" rx="1"/><rect x="9" y="6" width="6" height="9" rx="1"/></svg>
        <div><h4>MOBILE SERVICES</h4><p>Our comprehensive range of consulting services takes you from idea through development.</p></div>
      </div>
      <div class="feature">
        <svg width="16" height="16" viewBox="0 0 16 16"><path d="M8 14 2 8a3.3 3.3 0 0 1 6-4 3.3 3.3 0 0 1 6 4z" fill="#fff"/></svg>
        <div><h4>QUALITY THROUGH EXPERIENCE</h4><p>Our team of engineers know what it takes to serve more than 1,000,000 happy customers.</p></div>
      </div>
      <div class="feature">
        <svg width="16" height="16" viewBox="0 0 16 16" fill="none" stroke="#fff" stroke-width="1.2"><circle cx="8" cy="8" r="5"/><path d="M8 1v14M1 8h14"/></svg>
        <div><h4>I WANT YOU!</h4><p>KQ7 is always looking for talented developers. If you have what it takes - do not hesitate to contact us!</p></div>
      </div>
    </div>
  </section>

  <section class="intro abs">
    <h2>UNIQUE EXPERIENCES FOR<span>MOBILE</span></h2>
  </section>

  <section class="services abs">
    <div class="service current">
      <svg width="14" height="16" viewBox="0 0 14 16"><path d="M7 1C7 1 1 8 1 11a6 6 0 0 0 12 0C13 8 7 1 7 1z" fill="#fff"/></svg>
      <h3>NEEDS</h3>
      <p>Lorem Ipsum is simply dummy text of the printing and typesetting industry.</p>
      <a>Read more</a>
    </div>
    <div class="service">
      <svg width="14" height="16" viewBox="0 0 14 16" fill="var(--icon)"><path d="M7 0c3 3 4 6 3 10H4C3 6 4 3 7 0z"/><path d="M4 9 1 13h3zM10 9l3 4h-3z"/><rect x="6" y="11" width="2" height="4"/></svg>
      <h3>PLANNING AND<br>RAPID PROTOTYPING</h3>
      <p>Lorem Ipsum is simply dummy text of the printing and typesetting industry.</p>
      <a>Read more</a>
    </div>
    <div class="service">
      <svg width="14" height="16" viewBox="0 0 14 16" fill="none" stroke="var(--icon)" stroke-width="1.4"><rect x="2" y="1" width="10" height="14" rx="1.5"/><circle cx="7" cy="8" r="2.2"/></svg>
      <h3>CODING AND<br>TESTING</h3>
      <p>Lorem Ipsum is simply dummy text of the printing and typesetting industry.</p>
      <a>Read more</a>
    </div>
    <div class="service">
      <svg width="22" height="16" viewBox="0 0 22 16"><path d="M5 14a4 4 0 0 1 0-8 6 6 0 0 1 11-1 4.5 4.5 0 0 1 1 9z" fill="var(--icon)"/></svg>
      <h3>COMPLETION AND<br>MARKET INTRODUCTION</h3>
      <p>Lorem Ipsum is simply dummy text of the printing and typesetting industry.</p>
      <a>Read more</a>
    </div>
    <div class="service">
      <svg width="18" height="16" viewBox="0 0 18 16" fill="var(--icon)"><rect x="1" y="11" width="3" height="4"/><rect x="6" y="8" width="3" height="7"/><rect x="11" y="5" width="3" height="10"/><path d="M1 8 8 3l3 2 6-4" stroke="var(--icon)" stroke-width="1.2" fill="none"/></svg>
      <h3>ANALYSIS &amp;<br>IMPROVEMENTS</h3>
      <p>Lorem Ipsum is simply dummy text of the printing and typesetting industry.</p>
      <a>Read more</a>
    </div>
  </section>

  <section class="about abs">
    <div class="about-text abs">
      <h2 class="col-title">ABOUT US</h2>
      <p class="col-text">KQ7 Ventra is a specialty mobile solutions provider with expertise across all the major mobile platforms. We have a track record with several apps reaching the top 10 most downloaded lists. Deep knowledge of how to create and manage robust and intuitive apps has been acquired by the experience rendered from serving 1,000,000 customers.</p>
      <p class="more">Read more</p>
    </div>
    <div class="video abs" role="img" aria-label="Video still of a businessman holding a phone with floating app icons">
      <svg class="play abs" width="30" height="30" viewBox="0 0 30 30"><circle cx="15" cy="15" r="13" fill="#2a8fd8" stroke="#fff" stroke-width="2"/><path d="M12 9l9 6-9 6z" fill="#fff"/></svg>
    </div>
    <div class="testimonials abs">
      <h2 class="col-title">CUSTOMERS ARE SAYING</h2>
      <div class="avatars">
        <div class="avatar on" role="img" aria-label="Customer portrait placeholder"></div>
        <div class="avatar" role="img" aria-label="Customer portrait placeholder"></div>
        <div class="avatar" role="img" aria-label="Customer portrait placeholder"></div>
      </div>
      <p class="col-text">Lorem Ipsum is simply dummy text of the printing and typesetting industry.</p>
      <p class="more" style="margin-top:5px">Read more</p>
    </div>
  </section>

  <section class="facts-head abs">
    <h2>A FACT WORTH A THOUSAND WORDS,<span>OUR CLIENTS LOVE US AND WHY THEY KEEP COMING BACK</span></h2>
  </section>

  <section class="facts abs">
    <div class="phone abs" role="img" aria-label="Smartphone showing a word puzzle game">
      <div class="phone-screen abs"></div>
    </div>
    <div class="stats abs">
      <div class="stat"><b>1,000,000</b><span>HAPPY CUSTOMERS</span></div>
      <div class="op">+</div>
      <div class="stat"><b>X YEARS</b><span>OFF EXPERIENCE</span></div>
      <div class="op">+</div>
      <div class="stat"><b>FAMOUS</b><span>APPLICATIONS</span></div>
      <div class="op">=</div>
      <div class="stat red"><b>100%</b><span>SATISFACTION</span></div>
    </div>
    <div class="laptop abs" role="img" aria-label="Laptop showing a code editor">
      <div class="laptop-screen abs"></div>
    </div>
  </section>

  <section class="partners abs" aria-label="Technologies">
    <span class="chev">‹</span>
    <span class="badge"></span><span class="badge"></span><span class="badge"></span>
    <span class="badge"></span><span class="badge"></span><span class="badge"></span>
    <span class="chev">›</span>
  </section>

  <footer class="footer abs">
    <div class="f-brand abs">
      <div class="brand" style="display:flex;gap:3px;align-items:center"><span class="brand-mark"></span><span class="brand-name">KQ7</span></div>
      <p class="f-text" style="margin-top:6px">KQ7 Ventra is a specialty mobile solutions provider with expertise across all the major mobile platforms.</p>
    </div>
    <div class="f-menu abs">
      <div class="f-title">MENU</div>
      <ul><li class="active">HOME</li><li>OUR SERVICES</li><li>LATEST NEWS</li><li>CONTACT</li></ul>
    </div>
    <div class="f-contact abs">
      <div class="f-title">CONTACT US</div>
      <div class="f-row" style="margin-top:8px">
        <svg width="5" height="7" viewBox="0 0 5 7"><path d="M2.5 7S0 4 0 2.5a2.5 2.5 0 0 1 5 0C5 4 2.5 7 2.5 7z" fill="#888"/></svg>
        <p class="f-text">ADDRESS: HARLOW YARD 4, FINCH LANE, BRINDMOOR, WESTSHIRE BM3 9QL UNITED KINGDOM</p>
      </div>
      <div class="f-row">
        <svg width="5" height="6" viewBox="0 0 5 6"><rect x="0.5" y="0" width="4" height="6" rx="1" fill="#888"/></svg>
        <p class="f-text">PHONE: +00 0000 000</p>
      </div>
      <div class="f-row">
        <svg width="5" height="5" viewBox="0 0 5 5"><rect width="5" height="4" y="0.5" fill="#888"/></svg>
        <p class="f-text">EMAIL: MAIL@EXAMPLE.COM</p>
      </div>
    </div>
    <div class="f-follow abs">
      <div class="f-title">FOLLOW US</div>
      <div class="socials"><i></i><i></i><i></i><i></i></div>
      <div class="f-text" style="margin-top:6px">SIGN UP FOR OUR NEWSLETTER:</div>
      <div class="newsletter">Enter your email adress here...</div>
    </div>
  </footer>
  <div class="copyright abs">COPYRIGHT KQ7 VENTRA 2013. ALL RIGHTS RESERVED.</div>

</div>
</body>
</html>
```